Business card design needed

Our modern electrical contracting company requires business card design utilising our logo and incorporating our tag line "Service when you need it". We specialise in assisting our customers 24/7 offering a breakdown service.

Industry/Entity Type

Electrical

Contact Information for Business Card

Marcus Penfold, Electrical contractor,Tel: (08) 8546 3071, Fax: (08) 8679 4305, Mob 0428 736 514, Email: marcus.penfold@brightwirepower.com.au, Web: www.brightwirepower.com.au

Requirements
Must have
• we require a 2 sided card.
Front- Logo, tag line and contact information.
Rear- service when you need it! Call now for our 24/7 breakdown service

```html
<!DOCTYPE html>
<html lang="en">
<head>
<meta charset="utf-8">
<title>Brightwire Power – Business Card</title>
<link href="https://fonts.googleapis.com/css2?family=PT+Sans:wght@400;700&family=PT+Sans+Narrow:wght@400&display=swap" rel="stylesheet">
<style>
  :root {
    --page-bg: #ece9e6;
    --metal-dark: #6f7275;
    --metal-mid: #a9acaf;
    --metal-light: #e6e7e8;
    --panel: rgba(255,255,255,0.42);
    --brand-blue: #1f4fa3;
    --ink: #111111;
    --text: #4a4a4a;
    --text-soft: #777777;
    --divider: #6a6d70;
  }
  * { margin: 0; padding: 0; box-sizing: border-box; }
  html, body { width: 1200px; height: 933px; overflow: hidden; }
  body {
    background: var(--page-bg);
    font-family: "PT Sans", "Helvetica Neue", Arial, sans-serif;
    position: relative;
  }
  .card {
    position: absolute;
    left: 272px;
    width: 708px;
    height: 409px;
    overflow: hidden;
    background:
      linear-gradient(90deg, rgba(80,82,85,0.35) 0%, rgba(255,255,255,0) 18%, rgba(255,255,255,0) 82%, rgba(80,82,85,0.35) 100%),
      linear-gradient(180deg, var(--metal-dark) 0%, var(--metal-mid) 18%, var(--metal-light) 45%, var(--metal-light) 60%, var(--metal-mid) 82%, var(--metal-dark) 100%);
  }
  .card--front { top: 24px; }
  .card--back { top: 477px; }

  .panel {
    position: absolute;
    background: linear-gradient(90deg, rgba(255,255,255,0) 0%, var(--panel) 12%, var(--panel) 88%, rgba(255,255,255,0) 100%);
  }
  .card--front .panel { left: 101px; top: 127px; width: 460px; height: 140px; }
  .card--back .panel { left: 0; top: 129px; width: 708px; height: 180px; }

  .brand-mark {
    position: absolute;
    left: 146px; top: 146px;
    width: 66px; height: 66px;
    border-radius: 50%;
    background: var(--brand-blue);
  }
  .brand-name {
    position: absolute;
    left: 40px; top: 218px;
    width: 280px;
    text-align: center;
    font-size: 25px;
    font-weight: 700;
    color: var(--brand-blue);
    letter-spacing: 0.5px;
  }
  .divider {
    position: absolute;
    left: 337px; top: 169px;
    width: 2px; height: 80px;
    background: var(--divider);
  }
  .contact {
    position: absolute;
    left: 365px; top: 138px;
    color: var(--text);
  }
  .contact__name, .contact__role { font-size: 20px; line-height: 28px; }
  .contact__line { font-size: 14px; line-height: 20px; color: #333; }
  .contact__role { margin-bottom: 2px; }

  .tagline {
    position: absolute;
    left: 0; width: 708px;
    text-align: center;
  }
  .tagline--front {
    top: 278px;
    font-size: 32px;
    color: var(--text);
    padding-left: 12px;
  }
  .web-details {
    position: absolute;
    left: 0; top: 322px; width: 720px;
    text-align: center;
    font-size: 14px;
    line-height: 22px;
    color: var(--text);
  }

  .tagline--back {
    top: 162px;
    font-family: "PT Sans Narrow", "Arial Narrow", sans-serif;
    font-size: 50px;
    color: var(--ink);
    padding-left: 30px;
  }
  .call-line {
    position: absolute;
    left: 0; width: 708px;
    text-align: center;
    padding-left: 30px;
    font-family: "PT Sans Narrow", "Arial Narrow", sans-serif;
  }
  .call-line--offer { top: 241px; font-size: 20px; color: var(--text); }
  .call-line--phone { top: 271px; font-size: 20px; color: var(--text-soft); }
</style>
</head>
<body>
  <section class="card card--front" aria-label="Card front">
    <div class="panel"></div>
    <div class="brand-mark"></div>
    <div class="brand-name">BRIGHTWIRE POWER</div>
    <div class="divider"></div>
    <div class="contact">
      <p class="contact__name">Marcus Penfold</p>
      <p class="contact__role">Electrical contractor</p>
      <p class="contact__line">Tel: (08) 8546 3071,</p>
      <p class="contact__line">Fax: (08) 8679 4305,</p>
      <p class="contact__line">Mob 0428 736 514,</p>
    </div>
    <p class="tagline tagline--front">service when you need it!</p>
    <div class="web-details">
      <p>Email: marcus.penfold@brightwirepower.com.au</p>
      <p>Web: www.brightwirepower.com.au</p>
    </div>
  </section>

  <section class="card card--back" aria-label="Card back">
    <div class="panel"></div>
    <p class="tagline tagline--back">SERVICE WHEN YOU NEED IT!</p>
    <p class="call-line call-line--offer">CALL NOW FOR OUR 24/7 BREAKDOWN SERVICE</p>
    <p class="call-line call-line--phone">(08) 8546 3071</p>
  </section>
</body>
</html>
```